New Business Card Design Project

We are a Nationally ranked independent premium furniture retailer, and we want to show that. I am looking for a fresh look, double sided, modern card.. Open to any ideas or designs.

Target Market(s)

Looking to hit men/women 35-50.

Industry/Entity Type

Business

Contact Information for Business Card

Looking for a clean modern look. With that being said, we are wanting to highlight some of the awards that we have received ( Velmora Top 100 and top 16 Brisset Select, imagines linked). Also need website on card- www.shopvrn-example.com, and follow us; facebook, instagram, twitter (small thumbnails work best for those 3) Would like website, social media info, and two awards on backside with some imagery (we are a furniture, mattress and appliance business) and then logo, name, title address on front side

Colors

Designer to choose colors to be used in the design.

Requirements
Must have
• Company name, address, website, two awards, social media ques
Should not have
• cartoons

```html
<!DOCTYPE html>
<html lang="en">
<head>
<meta charset="utf-8">
<title>VRN Home Furnishings – Business Card</title>
<link rel="stylesheet" href="https://fonts.googleapis.com/css2?family=Open+Sans:wght@400;600;700&family=Oswald:wght@600&display=swap">
<style>
  :root {
    --backdrop: #2b2b2d;
    --card: #f4f4f3;
    --red: #c8372d;
    --navy: #1d3a72;
    --ink: #1f1f1f;
    --grey: #8b8b8b;
    --badge-grey: #9a9a9a;
  }
  * { box-sizing: border-box; margin: 0; padding: 0; }
  html, body { width: 799px; height: 1200px; overflow: hidden; }
  body {
    background: var(--backdrop);
    font-family: "Open Sans", Arial, sans-serif;
    color: var(--ink);
    position: relative;
  }
  .card {
    position: absolute;
    left: 70px;
    width: 660px;
    height: 377px;
    background: var(--card);
    border-radius: 24px;
    overflow: hidden;
    box-shadow: 0 14px 30px rgba(0,0,0,.45);
  }
  .card--front { top: 120px; }
  .card--back { top: 700px; }

  /* front */
  .watermark {
    position: absolute; left: 170px; top: 90px;
    font-size: 64px; font-weight: 700; color: rgba(0,0,0,.045);
    white-space: nowrap;
  }
  .award { position: absolute; text-align: center; }
  .award--top100 { left: 150px; top: 60px; width: 200px; }
  .award--select { left: 390px; top: 80px; width: 190px; }
  .award__note { font-size: 11px; color: #555; line-height: 1.25; margin-bottom: 8px; }
  .award__shape { display: block; margin: 0 auto; }
  .award__title { font-size: 17px; font-weight: 700; color: var(--navy); margin-top: 8px; }
  .award--select .award__title { color: #555; font-size: 14px; font-weight: 600; }
  .award__link { font-size: 10px; color: var(--grey); margin-top: 4px; }

  .follow {
    position: absolute; left: 28px; top: 292px;
    display: flex; align-items: center; gap: 6px;
    font-size: 15px; color: var(--ink);
  }
  .follow__dot { width: 16px; height: 16px; border-radius: 50%; background: var(--navy); }
  .follow__dot--alt { background: #4a77b8; }
  .follow__dot--pink { background: #b8457a; }

  .edge-line { position: absolute; left: 0; bottom: 0; width: 100%; height: 8px; background: var(--navy); }
  .web-tab {
    position: absolute; right: 0; bottom: 0; width: 320px; height: 62px;
    background: var(--red); border-top-left-radius: 26px;
    display: flex; align-items: center; justify-content: center;
    color: #fff; font-size: 19px; letter-spacing: .3px;
  }

  /* back */
  .person { position: absolute; left: 36px; top: 36px; }
  .person__name { font-family: "Oswald", "Arial Narrow", sans-serif; font-weight: 600; font-size: 26px; color: var(--red); line-height: 1.1; }
  .person__title { font-size: 13px; color: var(--ink); }

  .contact { position: absolute; left: 36px; top: 178px; list-style: none; font-size: 15px; line-height: 1.35; }
  .contact li { display: flex; align-items: center; gap: 10px; }
  .contact svg { width: 13px; height: 13px; fill: var(--red); flex: none; }
  .contact__address { margin-top: 2px; font-size: 15px; line-height: 1.3; }

  .brand {
    position: absolute; right: 40px; bottom: 46px;
    display: flex; align-items: center; gap: 12px;
  }
  .brand__mark { width: 26px; height: 26px; background: var(--navy); }
  .brand__name { font-size: 34px; font-weight: 700; color: var(--red); line-height: 1; }
</style>
</head>
<body>

<section class="card card--front" aria-label="Card front">
  <div class="watermark">VRN Home Furnishings</div>

  <div class="award award--top100">
    <p class="award__note">Proud to be one of Velmora's<br>Top Private Companies</p>
    <svg class="award__shape" width="150" height="90" role="img" aria-label="Velmora Top 100 award badge">
      <rect x="0" y="0" width="150" height="90" rx="6" fill="var(--badge-grey)"/>
    </svg>
    <p class="award__title">Velmora Top 100</p>
    <p class="award__link">velmoratimes-example.com/top100</p>
  </div>

  <div class="award award--select">
    <svg class="award__shape" width="120" height="120" role="img" aria-label="Brisset Select ranking seal">
      <circle cx="60" cy="60" r="56" fill="var(--red)"/>
    </svg>
    <p class="award__title">top 16 Brisset Select</p>
  </div>

  <div class="follow">
    <span>Follow us:</span>
    <span class="follow__dot"></span>
    <span class="follow__dot follow__dot--alt"></span>
    <span class="follow__dot follow__dot--pink"></span>
  </div>

  <div class="edge-line"></div>
  <div class="web-tab">www.shopvrn-example.com</div>
</section>

<section class="card card--back" aria-label="Card back">
  <div class="person">
    <p class="person__name">Daniel Arlow</p>
    <p class="person__title">Managing Director</p>
  </div>

  <ul class="contact">
    <li>
      <svg viewBox="0 0 24 24"><path d="M6.6 10.8a15 15 0 0 0 6.6 6.6l2.2-2.2a1 1 0 0 1 1-.25 11.4 11.4 0 0 0 3.6.57 1 1 0 0 1 1 1V20a1 1 0 0 1-1 1A17 17 0 0 1 3 4a1 1 0 0 1 1-1h3.5a1 1 0 0 1 1 1c0 1.25.2 2.45.57 3.57a1 1 0 0 1-.25 1z"/></svg>
      (555) 014-2288
    </li>
    <li>
      <svg viewBox="0 0 24 24"><path d="M2 5h20v14H2z M2 5l10 8 10-8" stroke="#fff" stroke-width="1.5"/></svg>
      contactus@shopvrn-example.com
    </li>
    <li>
      <svg viewBox="0 0 24 24"><circle cx="12" cy="12" r="10"/><path d="M2 12h20M12 2c3 3 3 17 0 20M12 2c-3 3-3 17 0 20" stroke="#fff" stroke-width="1.3" fill="none"/></svg>
      www.shopvrn-example.com
    </li>
    <li class="contact__address">42 Larkspur Ave.<br>Velmora City 10482</li>
  </ul>

  <div class="brand">
    <span class="brand__mark"></span>
    <span class="brand__name">VRN Home Furnishings</span>
  </div>
</section>

</body>
</html>
```